Retail Sign for Houseplant Campaign

Please make Portrait style not landscape Sign will measure 3 to 4 foot tall by 22.2inches and place on rolling racks of houseplants for a retail promotion in The Yard Locker. The theme of the promotion will be "Bring your home to life with Houseplants!" Selling points which should be on the sign are Houseplants * improve your mood * reduce fatigue * improve focus. Please put signage in landscape format and include yard locker and verdant makings logo.

Just recovered from covid. Im sorry for the delay

Target Market(s)

People who love plants

Industry/Entity Type

Retail

Colors
00AB8E
00BBA5
67D7C9
C6EFE9
E9F9F6
59FF00
82FF00
B8FF75
E3FFCB
F4FFEA
FFF300
FFF600
FEFA6F
FFFEC7
FFFEE8
FFC000
F8CF3A
FAE287
FDF2CF
FEFAEE

Requirements
Must have
• Must feel energetic and encourage people to buy plants. Should include 1-2 photos and the selling points listed

```html
<!DOCTYPE html>
<html lang="en">
<head>
<meta charset="utf-8">
<title>Bring Your Home to Life with Houseplants</title>
<link rel="stylesheet" href="https://fonts.googleapis.com/css2?family=Josefin+Sans:wght@400;500&family=Great+Vibes&display=swap">
<style>
  :root {
    --page: #ffffff;
    --green: #1ec96a;
    --yellow: #fff35a;
    --yellow-soft: #fef06f;
    --orange: #ffc000;
    --orange-deep: #ffad1f;
    --ink: #111111;
    --ring: #ffffff;
    --leaf-dark: #1f5e2a;
    --leaf-mid: #3f8f3a;
    --leaf-light: #8cc85a;
    --pot-white: #f4f4f2;
    --studio-grey: #e3e6e3;
    --shirt-teal: #6f9c9a;
    --hair-brown: #6b4a35;
  }
  html, body {
    margin: 0;
    padding: 0;
    width: 1200px;
    height: 2180px;
    overflow: hidden;
    background: var(--page);
  }
  .canvas {
    position: relative;
    width: 1200px;
    height: 2180px;
    background: var(--page);
  }
  .sign {
    position: absolute;
    left: 172px;
    top: 160px;
    width: 856px;
    height: 1860px;
    overflow: hidden;
    background: linear-gradient(180deg,
      var(--green) 0%,
      #7fdc5a 14%,
      var(--yellow-soft) 28%,
      var(--yellow) 50%,
      #ffd43a 70%,
      var(--orange-deep) 100%);
  }
  .headline {
    position: absolute;
    top: 70px;
    left: 0;
    width: 100%;
    margin: 0;
    text-align: center;
    color: var(--ink);
    font-family: "Josefin Sans", sans-serif;
    font-weight: 400;
  }
  .headline .line {
    display: block;
    font-size: 74px;
    line-height: 84px;
  }
  .headline .script {
    display: block;
    font-family: "Great Vibes", cursive;
    font-size: 124px;
    line-height: 140px;
    margin-top: 8px;
  }
  .rings {
    position: absolute;
    left: 0;
    top: 0;
  }
  .photo-person {
    position: absolute;
    left: 316px;
    top: 408px;
    width: 624px;
    height: 624px;
    border-radius: 50%;
    background:
      radial-gradient(ellipse 22% 30% at 58% 70%, rgba(255,255,255,0.85) 0%, transparent 100%),
      radial-gradient(ellipse 26% 34% at 42% 80%, rgba(111,156,154,0.85) 0%, transparent 100%),
      radial-gradient(ellipse 16% 24% at 42% 45%, rgba(107,74,53,0.8) 0%, transparent 100%),
      radial-gradient(ellipse 30% 30% at 66% 38%, rgba(63,143,58,0.75) 0%, transparent 100%),
      radial-gradient(circle at 50% 50%, #fff39a 0%, #ffe35a 60%, #ffd23a 100%);
  }
  .photo-plant {
    position: absolute;
    left: 8px;
    top: 516px;
    width: 416px;
    height: 416px;
    box-sizing: border-box;
    border-radius: 50%;
    border: 10px solid var(--ring);
    background:
      radial-gradient(ellipse 26% 22% at 52% 70%, var(--pot-white) 0%, var(--pot-white) 70%, transparent 100%),
      radial-gradient(ellipse 36% 26% at 50% 36%, rgba(31,94,42,0.9) 0%, rgba(63,143,58,0.6) 60%, transparent 100%),
      radial-gradient(circle at 50% 45%, #ffffff 0%, #eef0ee 65%, var(--studio-grey) 100%);
  }
  .selling-points {
    position: absolute;
    top: 1130px;
    left: 0;
    width: 100%;
    margin: 0;
    padding: 0;
    list-style: none;
    text-align: center;
    font-family: "Josefin Sans", sans-serif;
    font-weight: 500;
    color: var(--ink);
  }
  .selling-points li {
    width: 560px;
    margin: 0 auto;
    font-size: 56px;
    line-height: 84px;
    border-bottom: 2px solid rgba(0,0,0,0.35);
  }
  .selling-points li:last-child {
    border-bottom: none;
  }
  .foliage {
    position: absolute;
    left: 0;
    bottom: 0;
    width: 100%;
    height: 400px;
    background:
      radial-gradient(ellipse 22% 80% at 12% 100%, var(--leaf-dark) 0%, rgba(31,94,42,0.6) 60%, transparent 100%),
      radial-gradient(ellipse 20% 90% at 40% 100%, var(--leaf-mid) 0%, rgba(63,143,58,0.5) 60%, transparent 100%),
      radial-gradient(ellipse 18% 70% at 62% 100%, var(--leaf-light) 0%, transparent 100%),
      radial-gradient(ellipse 24% 95% at 86% 100%, var(--leaf-dark) 0%, rgba(63,143,58,0.55) 60%, transparent 100%),
      linear-gradient(180deg, rgba(63,143,58,0) 0%, rgba(63,143,58,0.35) 40%, var(--leaf-mid) 80%, var(--leaf-dark) 100%);
  }
</style>
</head>
<body>
<div class="canvas">
  <section class="sign">
    <h1 class="headline">
      <span class="line">Bring Your Home</span>
      <span class="line">to Life with</span>
      <span class="script">Houseplants!</span>
    </h1>

    <svg class="rings" width="856" height="1860" viewBox="0 0 856 1860" aria-hidden="true">
      <circle cx="216" cy="724" r="236" fill="none" stroke="var(--ring)" stroke-width="3" opacity="0.9"/>
      <circle cx="628" cy="720" r="344" fill="none" stroke="var(--ring)" stroke-width="3" opacity="0.9"/>
      <path d="M 0 500 Q 140 440 300 450" fill="none" stroke="var(--ring)" stroke-width="3" opacity="0.8"/>
      <path d="M 300 1050 Q 560 1090 856 1000" fill="none" stroke="var(--ring)" stroke-width="3" opacity="0.8"/>
    </svg>

    <div class="photo-person" role="img" aria-label="Photo of a smiling woman hugging a large potted monstera plant in a white pot"></div>
    <div class="photo-plant" role="img" aria-label="Photo of a monstera plant in a white pot on a wooden stand"></div>

    <ul class="selling-points">
      <li>Houseplants</li>
      <li>Improve your mood</li>
      <li>Reduce fatigue</li>
      <li>Improve focus</li>
    </ul>

    <div class="foliage" role="img" aria-label="Photo of assorted leafy green houseplants and snake plants along the bottom edge"></div>
  </section>
</div>
</body>
</html>
```